Business Card for Kinesiologist Practitioner

I need a logo and business card designing for a Kinesiologist Practitioner. I would like the card to be double sided. The look and feel of the logo and graphics should depict natural healing and well being. I would like a modern, fresh and contemporary design with a professional style. I have attached some logos and business cards that I liek from other natural health practitioners. I have also attached some logos that I like and a mock up of the business card style. Please however use your own creative input to change any element as you feel appropriate.

I have used the strap line "Quiet Renewal" which I would like underneath the logo. For the logo I like natural objects and possibly with 3 elements in the design as the course I have studied follows a "Open Arc " healing concept (mind, body, soul). Maybe a tree or flower with 3 elements and a representation or suggestion of the human body somehow. You will see from the logos i have uploaded

Industry/Entity Type

Business

Contact Information for Business Card

Please see the mock up attached.

Font styles to use
Serif
Sans Serif

Colors
faa54b
acd036
fbee3d
85cae6

Requirements
Must have
• Note the colours are just suggested colours. Please us your own creative licence.

```html
<!DOCTYPE html>
<html lang="en">
<head>
<meta charset="utf-8">
<title>Quiet Renewal – Business Card</title>
<link href="https://fonts.googleapis.com/css2?family=Open+Sans:wght@400;600&family=Oswald:wght@500&display=swap" rel="stylesheet">
<style>
  :root {
    --backdrop: #141414;
    --card: #ffffff;
    --orange: #f7a13e;
    --green: #a9cc35;
    --ink: #3a3a3a;
  }
  html, body {
    margin: 0;
    padding: 0;
    width: 1200px;
    height: 900px;
    overflow: hidden;
    background: var(--backdrop);
  }
  .stage {
    position: relative;
    width: 1200px;
    height: 900px;
  }
  .card {
    position: absolute;
    top: 306px;
    width: 439px;
    height: 271px;
    background: var(--card);
    border-radius: 10px;
  }
  .card--front { left: 149px; }
  .card--back { left: 609px; width: 440px; }

  .brand-mark {
    position: absolute;
    display: flex;
    flex-direction: column;
    align-items: center;
    gap: 10px;
  }
  .card--front .brand-mark {
    left: 52px;
    top: 78px;
    width: 130px;
  }
  .brand-mark__dot {
    width: 54px;
    height: 54px;
    border-radius: 50%;
    background: var(--green);
  }
  .brand-mark__name {
    font-family: "Oswald", "Arial Narrow", sans-serif;
    font-weight: 500;
    color: var(--orange);
    text-transform: uppercase;
    white-space: nowrap;
    line-height: 1;
  }
  .card--front .brand-mark__name { font-size: 20px; }

  .card--back .brand-mark {
    left: 0;
    right: 0;
    top: 64px;
    gap: 26px;
  }
  .card--back .brand-mark__dot { width: 72px; height: 72px; }
  .card--back .brand-mark__name { font-size: 38px; letter-spacing: 0.5px; }

  .contact {
    position: absolute;
    left: 222px;
    top: 60px;
    font-family: "Open Sans", Arial, sans-serif;
    color: var(--ink);
    font-size: 12px;
    line-height: 16px;
  }
  .contact__name {
    margin: 0;
    font-size: 14.5px;
    font-weight: 600;
    color: var(--orange);
    line-height: 18px;
  }
  .contact__role { margin: 0 0 10px; }
  .contact__address { margin: 0 0 11px; font-style: normal; }
  .contact__list { list-style: none; margin: 0; padding: 0; }
  .contact__list li {
    display: flex;
    align-items: center;
    gap: 7px;
  }
  .contact__icon { width: 9px; height: 9px; fill: var(--orange); flex: none; }
</style>
</head>
<body>
<main class="stage">
  <section class="card card--front" aria-label="Card front">
    <div class="brand-mark">
      <span class="brand-mark__dot"></span>
      <span class="brand-mark__name">Quiet Renewal</span>
    </div>
    <div class="contact">
      <p class="contact__name">Clara Whitfield</p>
      <p class="contact__role">Managing Director</p>
      <address class="contact__address">48 Willow Lane, Suite 2<br>Brookfield, 204518.</address>
      <ul class="contact__list">
        <li>
          <svg class="contact__icon" viewBox="0 0 10 10" aria-hidden="true"><path d="M2 0.5 L3.6 0.5 L4.3 2.8 L3.2 3.7 Q4.2 5.8 6.3 6.8 L7.2 5.7 L9.5 6.4 L9.5 8 Q9.5 9.5 8 9.5 Q0.5 8.8 0.5 2 Q0.5 0.5 2 0.5Z"/></svg>
          <span>044-210 987 654</span>
        </li>
        <li>
          <svg class="contact__icon" viewBox="0 0 10 10" aria-hidden="true"><path d="M0.5 2 H9.5 V8.5 H0.5Z M0.5 2 L5 5.5 L9.5 2" fill="var(--orange)"/><path d="M1 2.6 L5 5.6 L9 2.6" stroke="#fff" stroke-width="0.9" fill="none"/></svg>
          <span>hello@quietrenew.com</span>
        </li>
        <li>
          <svg class="contact__icon" viewBox="0 0 10 10" aria-hidden="true"><circle cx="5" cy="5" r="4.6"/><path d="M3 3.5 Q4.5 2.8 5 4 Q4 5.5 5.5 6.5 L6 8.5 Q3 8 2.2 5.5Z" fill="#fff"/></svg>
          <span>www.quietrenew.com</span>
        </li>
      </ul>
    </div>
  </section>

  <section class="card card--back" aria-label="Card back">
    <div class="brand-mark">
      <span class="brand-mark__dot"></span>
      <span class="brand-mark__name">Quiet Renewal</span>
    </div>
  </section>
</main>
</body>
</html>
```